Harbor Decals
Vending Solutions for your Business
Harbor Decals -
Creative Brief
Bright & Fun-filled
Dale Whitcombe
Owner
24870 Pellwood Lane San Jose, CA 95031
harbor.decals@pellmail.net
Use logo on card and stationary

```html
<!DOCTYPE html>
<html lang="en">
<head>
<meta charset="utf-8">
<title>Harbor Decals – Business Card Options</title>
<link href="https://fonts.googleapis.com/css2?family=PT+Sans:ital,wght@0,400;0,700;1,400&family=Michroma&display=swap" rel="stylesheet">
<style>
  :root {
    --board: #3b3b3b;
    --board-dark: #2c2c2c;
    --orange: #f39a1e;
    --orange-deep: #e07d10;
    --brand: #4a3d9c;
    --brand-light: #8a7de0;
    --ink: #444;
    --ink-light: #cfcfcf;
    --card-white: #ffffff;
    --card-black: #0c0c0c;
    --swoosh: #b9b9b9;
    --caption: #e6e6e6;
  }
  html, body {
    margin: 0;
    padding: 0;
    overflow: hidden;
  }
  body {
    width: 1200px;
    height: 809px;
    background: radial-gradient(ellipse at center, var(--board) 0%, var(--board-dark) 100%);
    position: relative;
    font-family: "PT Sans", Arial, sans-serif;
  }
  .card {
    position: absolute;
    width: 494px;
    border-radius: 14px;
    overflow: hidden;
    box-shadow: 0 2px 6px rgba(0,0,0,0.45);
  }
  .card--front { height: 331px; top: 29px; }
  .card--back { height: 286px; top: 422px; }
  .card--a { left: 77px; background: var(--card-white); color: var(--ink); }
  .card--b { left: 640px; background: var(--card-black); color: var(--ink-light); }

  .corner {
    position: absolute;
    top: 0;
    right: 0;
    width: 90px;
    height: 84px;
  }
  .brand {
    position: absolute;
    left: 31px;
    top: 43px;
    display: flex;
    align-items: center;
    gap: 12px;
  }
  .brand__dot {
    width: 72px;
    height: 72px;
    border-radius: 50%;
    background: radial-gradient(circle at 40% 35%, #ffc35a 0%, var(--orange) 55%, var(--orange-deep) 100%);
  }
  .brand__name {
    font-weight: 700;
    font-size: 36px;
    color: var(--brand);
    letter-spacing: -0.5px;
  }
  .card--b .brand__name { color: var(--brand-light); }
  .tagline {
    position: absolute;
    left: 150px;
    top: 116px;
    font-size: 12px;
    color: var(--orange-deep);
  }
  .person {
    position: absolute;
    right: 264px;
    top: 190px;
    text-align: right;
  }
  .person__name {
    font-size: 15px;
    font-weight: 700;
    color: var(--orange-deep);
  }
  .person__role {
    font-size: 11px;
    margin-top: 1px;
  }
  .person__address {
    font-size: 11px;
    font-style: italic;
    line-height: 17px;
    margin-top: 12px;
  }
  .divider {
    position: absolute;
    left: 238px;
    top: 176px;
    width: 1px;
    height: 104px;
    background: var(--orange);
  }
  .contact {
    position: absolute;
    left: 246px;
    top: 184px;
    border-collapse: collapse;
    font-size: 11px;
  }
  .contact td { padding: 0 0 9px 0; line-height: 12px; }
  .contact__label { color: var(--orange-deep); width: 72px; }

  .back-brand {
    position: absolute;
    inset: 0;
    display: flex;
    flex-direction: column;
    align-items: center;
    justify-content: center;
    gap: 8px;
  }
  .back-brand .brand__dot { width: 88px; height: 88px; }
  .back-brand .brand__name { font-size: 20px; }

  .caption {
    position: absolute;
    width: 494px;
    text-align: center;
    font-family: "Michroma", "Arial", sans-serif;
    font-size: 13px;
    letter-spacing: 2.5px;
    color: var(--caption);
  }
  .caption--a { left: 77px; }
  .caption--b { left: 640px; }
  .caption--front { top: 366px; }
  .caption--back { top: 726px; }
</style>
</head>
<body>

<svg width="0" height="0" style="position:absolute">
  <defs>
    <symbol id="corner-swoosh" viewBox="0 0 90 84">
      <path d="M14 0 H90 V84 C80 40 55 12 14 0 Z" fill="#f39a1e"/>
      <path d="M0 0 H14 C55 12 80 40 90 84 H84 C74 44 48 16 0 0 Z" fill="#b9b9b9"/>
    </symbol>
  </defs>
</svg>

<!-- Front A -->
<section class="card card--front card--a">
  <svg class="corner" viewBox="0 0 90 84"><use href="#corner-swoosh"/></svg>
  <div class="brand">
    <div class="brand__dot"></div>
    <div class="brand__name">Harbor Decals</div>
  </div>
  <div class="tagline">Vending Solutions for your Business</div>
  <div class="person">
    <div class="person__name">Dale Whitcombe</div>
    <div class="person__role">Owner</div>
    <div class="person__address">24870 Pellwood Lane<br>San Jose, CA 95031</div>
  </div>
  <div class="divider"></div>
  <table class="contact">
    <tr><td class="contact__label">Toll free</td><td>1-800-555-0142</td></tr>
    <tr><td class="contact__label">Phone</td><td>408-555-0187</td></tr>
    <tr><td class="contact__label">Fax</td><td>408-555-0163</td></tr>
    <tr><td class="contact__label">Email</td><td>harbor.decals@pellmail.net</td></tr>
  </table>
</section>
<div class="caption caption--a caption--front">BUSINESS CARD FRONT OPTION A</div>

<!-- Front B -->
<section class="card card--front card--b">
  <svg class="corner" viewBox="0 0 90 84"><use href="#corner-swoosh"/></svg>
  <div class="brand">
    <div class="brand__dot"></div>
    <div class="brand__name">Harbor Decals</div>
  </div>
  <div class="tagline">Vending Solutions for your Business</div>
  <div class="person">
    <div class="person__name">Dale Whitcombe</div>
    <div class="person__role">Owner</div>
    <div class="person__address">24870 Pellwood Lane<br>San Jose, CA 95031</div>
  </div>
  <div class="divider"></div>
  <table class="contact">
    <tr><td class="contact__label">Toll free</td><td>1-800-555-0142</td></tr>
    <tr><td class="contact__label">Phone</td><td>408-555-0187</td></tr>
    <tr><td class="contact__label">Fax</td><td>408-555-0163</td></tr>
    <tr><td class="contact__label">Email</td><td>harbor.decals@pellmail.net</td></tr>
  </table>
</section>
<div class="caption caption--b caption--front">BUSINESS CARD FRONT OPTION B</div>

<!-- Back A -->
<section class="card card--back card--a">
  <div class="back-brand">
    <div class="brand__dot"></div>
    <div class="brand__name">Harbor Decals</div>
  </div>
</section>
<div class="caption caption--a caption--back">BUSINESS CARD BACK OPTION A</div>

<!-- Back B -->
<section class="card card--back card--b">
  <div class="back-brand">
    <div class="brand__dot"></div>
    <div class="brand__name">Harbor Decals</div>
  </div>
</section>
<div class="caption caption--b caption--back">BUSINESS CARD BACK OPTION B</div>

</body>
</html>
```